I would like to update my one-page service sheet to provide a more professional/polished look and...

One page service sheet - with content on both the front and back. I've uploaded my current one page service sheet to provide background. I've also included a service sheet that I recently received from another business owner (from a very different business) that is a representation of the kind of feel I'm looking for. My business website may be found at: www.morvitelconsulting.com

```html
<!DOCTYPE html>
<html lang="en">
<head>
<meta charset="utf-8">
<title>Morvitel Consulting – Service Sheet</title>
<link rel="stylesheet" href="https://fonts.googleapis.com/css2?family=Montserrat:wght@500;600;700;800&family=Lato:ital,wght@0,400;0,700;1,400&display=swap">
<style>
  :root {
    --orange: #ee7623;
    --slate: #3b4658;
    --ink: #2b2b2b;
    --paper: #ffffff;
    --backdrop: #e2e3e5;
  }
  * { margin: 0; padding: 0; box-sizing: border-box; }
  html, body { width: 1200px; height: 786px; overflow: hidden; }
  body {
    background: var(--backdrop);
    font-family: "Lato", Arial, sans-serif;
    color: var(--ink);
    position: relative;
  }
  .page {
    position: absolute;
    top: 43px;
    width: 540px;
    height: 699px;
    background: var(--paper);
    overflow: hidden;
  }
  .page--front { left: 46px; }
  .page--back { left: 614px; }

  /* Front page */
  .hero-photo {
    position: absolute; left: 0; top: 0; width: 540px; height: 358px;
    background: linear-gradient(180deg, #8e9296 0%, #c7b08a 30%, #e9a04a 45%, #b9b3aa 58%, #6f6d6a 70%, #1e1c1b 82%, #0d0d0d 100%);
  }
  .hero-title {
    position: absolute; left: 0; top: 37px; width: 540px;
    text-align: center;
    font-family: "Montserrat", Arial, sans-serif;
    font-weight: 700; font-size: 27px; line-height: 32px;
    color: var(--slate);
  }
  .hero-rule {
    position: absolute; left: 194px; top: 104px; width: 152px; height: 2px;
    background: var(--slate);
  }
  .hero-service {
    position: absolute; left: 0; top: 322px; width: 540px;
    text-align: center;
    font-family: "Montserrat", Arial, sans-serif;
    font-weight: 800; font-size: 25px; letter-spacing: 0.2px;
    color: var(--orange);
  }
  .banner {
    position: absolute; left: 28px; top: 358px; width: 484px; height: 27px;
  }
  .banner-text {
    position: absolute; left: 0; top: 364px; width: 540px;
    text-align: center; color: #fff;
    font-family: "Montserrat", Arial, sans-serif; font-weight: 500; font-size: 12.5px;
  }

  .service-list {
    position: absolute; list-style: none;
    font-size: 10.4px; line-height: 14.4px;
  }
  .service-list li { position: relative; }
  .service-list li::before {
    content: "•"; position: absolute; left: -31px; top: 0;
  }
  .service-list .lead { color: var(--orange); font-weight: 700; }
  .page--front .service-list { left: 66px; top: 408px; width: 400px; }

  .quote-box {
    position: absolute; left: 61px; top: 542px; width: 420px; height: 60px;
    border: 2.5px solid var(--slate);
    text-align: center;
  }
  .quote-text {
    font-style: italic; font-size: 17px; line-height: 21px; color: var(--slate);
    padding-top: 6px;
  }
  .quote-author {
    position: absolute; left: 50%; bottom: -9px; transform: translateX(-50%);
    background: var(--paper); padding: 0 18px;
    font-style: italic; font-weight: 400; font-size: 12px; color: var(--orange);
    letter-spacing: 0.3px;
  }

  .footer-band { position: absolute; left: 0; top: 626px; width: 540px; height: 57px; }
  .contact {
    position: absolute; left: 34px; top: 636px;
    font-family: "Montserrat", Arial, sans-serif; font-weight: 600; font-style: normal;
    font-size: 10.4px; line-height: 13px; color: #fff;
  }
  .brand {
    position: absolute; left: 326px; top: 646px; width: 170px;
    display: flex; align-items: center; justify-content: center; gap: 6px;
    font-family: "Montserrat", Arial, sans-serif; font-weight: 700;
    font-size: 12.5px; color: var(--slate);
  }
  .brand-mark { width: 9px; height: 9px; background: var(--slate); flex: none; }

  /* Back page */
  .section-title {
    position: absolute;
    font-family: "Montserrat", Arial, sans-serif;
    font-weight: 800; font-size: 30px; line-height: 32px;
    color: var(--orange);
  }
  .section-sub {
    position: absolute;
    font-family: "Montserrat", Arial, sans-serif;
    font-weight: 500; font-size: 13.5px; line-height: 17.5px;
  }
  .process-title { left: 35px; top: 43px; }
  .process-sub { left: 35px; top: 136px; width: 235px; color: var(--ink); }
  .process-photo {
    position: absolute; left: 270px; top: 38px; width: 237px; height: 152px;
    background: linear-gradient(200deg, #2f6fb3 0%, #5b93cc 45%, #a9c6e2 80%, #dfe8ef 100%);
  }
  .page--back .process-list { left: 66px; top: 215px; width: 416px; }

  .solutions-panel {
    position: absolute; left: 0; top: 350px; width: 540px; height: 349px;
    background: var(--slate);
  }
  .solutions-photo {
    position: absolute; left: 34px; top: 375px; width: 238px; height: 152px;
    background: radial-gradient(ellipse at 55% 45%, #5aa6e8 0%, #1f5aa0 35%, #0c1f3d 75%, #070d1a 100%);
  }
  .solutions-title { left: 286px; top: 384px; }
  .solutions-sub { left: 286px; top: 483px; width: 240px; color: #fff; }
  .page--back .solutions-list { left: 66px; top: 549px; width: 428px; color: #fff; }
</style>
</head>
<body>

<section class="page page--front">
  <div class="hero-photo" role="img" aria-label="Silhouetted team of hikers climbing a mountain ridge above a sea of clouds at sunset"></div>
  <h1 class="hero-title">Replace Confusion and Hesitation<br>Withclarity and Resolve.</h1>
  <div class="hero-rule"></div>
  <h2 class="hero-service">GROWTH STRATEGY &amp; INNOVATION</h2>

  <svg class="banner" width="484" height="27" viewBox="0 0 484 27" aria-hidden="true">
    <polygon points="0,0 484,0 470,27 14,27" fill="#3b4658"/>
  </svg>
  <p class="banner-text">Discover what’s needed to reach the next stage of growth.</p>

  <ul class="service-list">
    <li><span class="lead">Growth Strategy &amp; Business Model Review.</span> Gain an objective perspective on your growth strategy and business.</li>
    <li><span class="lead">Revenue Acceleration&amp; Lead Generation.</span> Define and execute strategies and tactics to drive demand and top line growth.</li>
    <li><span class="lead">Execution and Scale.</span> Enable your people, processes, and technology to meet the demands of growth.</li>
    <li><span class="lead">Pricing Strategies.</span> Strategically price products and services.</li>
    <li><span class="lead">Growth Training.</span> Group and individual training/coaching.</li>
  </ul>

  <blockquote class="quote-box">
    <p class="quote-text">“We are what we repeatedly do. Excellence,<br>therefore, is not an act, but a habit."</p>
    <cite class="quote-author">THERON VALE</cite>
  </blockquote>

  <svg class="footer-band" width="540" height="57" viewBox="0 0 540 57" aria-hidden="true">
    <polygon points="0,0 322,0 306,57 0,57" fill="#ee7623"/>
    <polygon points="510,0 540,0 540,57 494,57" fill="#ee7623"/>
  </svg>
  <address class="contact">
    Dana Kerlow | 651.555.0142<br>
    admin@morvitelconsulting.com<br>
    www.morvitelconsulting.com
  </address>
  <div class="brand">
    <span class="brand-mark"></span>
    <span class="brand-name">Morvitel Consulting</span>
  </div>
</section>

<section class="page page--back">
  <h2 class="section-title process-title">GROWTH<br>PROCESS &amp;<br>EXECUTION</h2>
  <p class="section-sub process-sub">Fine-tune and formalize<br>growth processes for efficiency,<br>effectiveness, and scale.</p>
  <div class="process-photo" role="img" aria-label="Formation of aerobatic jets trailing white smoke against a blue sky, one breaking away upward"></div>

  <ul class="service-list process-list">
    <li><span class="lead">Innovation Capture &amp; Elaboration.</span>Standardize ideacapture, analysis, funding, elaboration, and innovation roll-out.</li>
    <li><span class="lead">Growth Channel Optimization.</span> Enhance the prospect and customer experience by blending digital and traditional.</li>
    <li><span class="lead">Business Development.</span> Transform business development into a proactive “team sport” and increase accountability.</li>
    <li><span class="lead">Prospect&amp; ClientExperience Mapping.</span> Create greater client stickiness, brand resonance, and be “easier to do business with.”</li>
  </ul>

  <div class="solutions-panel"></div>
  <div class="solutions-photo" role="img" aria-label="Hands holding a tablet projecting glowing blue business and analytics icons"></div>
  <h2 class="section-title solutions-title">GROWTH<br>SOLUTIONS &amp;<br>ANALYTICS</h2>
  <p class="section-sub solutions-sub">Get the right capabilities in place to support your growth journey.</p>

  <ul class="service-list solutions-list">
    <li><span class="lead">Technology Strategy &amp;Roadmap.</span> Ensure that the right technology is in place for each step of your growth journey.</li>
    <li><span class="lead">Software Selection.</span> Identify the specific capabilities and vendors that are most appropriate for your business.</li>
    <li><span class="lead">Project Leadership.</span> Get critical projects over the finish line.</li>
    <li><span class="lead">Disruptive Trends.</span> Demystify “Digital,” “Big Data,” “Artificial Intelligence,” and “Internet of Things” to create advantage.</li>
    <li><span class="lead">Critical Metrics.</span> Determine the leading and lagging metrics that are most critical for your business.</li>
  </ul>
</section>

</body>
</html>
```